FLYER: Human Factors in Traffic Crashes - Analysis of Drivers' Responses - training

We are hosting a class in Australia 30, November to 4, December 2020. I would like to have a flyer designed to "sell" the class with description of course topics. I have uploaded a flyer I started on my own but I want it to be professional. Dr. Pelloway only gets to AU every 3-5 years to teach from the US. I would like to have some type of roadway scenery, prefer a nighttime scene.

Target Market(s)

Accident reconstructionists and engineers, police reconstructionists.

Font styles to use
Serif

Colors
fec214

Requirements
Must have
• Name of course and course topics, location of course, price, website and contact information.
Nice to have
• Some type of roadway background, possibly a nighttime scene on a roadway.

```html
<!DOCTYPE html>
<html lang="en">
<head>
<meta charset="utf-8">
<title>Human Factors in Traffic Crashes – Open Class</title>
<link href="https://fonts.googleapis.com/css2?family=Montserrat:wght@400;700;800&display=swap" rel="stylesheet">
<style>
  :root {
    --gold: #fec214;
    --ink: #1e1e1e;
    --text: #2f2f2f;
    --white: #ffffff;
    --night: #141a3a;
    --footer: #232323;
  }
  * { margin: 0; padding: 0; box-sizing: border-box; }
  html, body { width: 935px; height: 1200px; overflow: hidden; background: var(--white); }
  body { font-family: "Montserrat", Arial, sans-serif; color: var(--text); position: relative; }

  .brand-header { position: absolute; left: 0; top: 0; width: 935px; height: 170px; background: var(--white);
    display: flex; align-items: center; justify-content: center; gap: 14px; }
  .brand-mark { width: 34px; height: 34px; border-radius: 50%; background: var(--gold); }
  .brand-name { font-weight: 800; font-size: 34px; color: var(--ink); letter-spacing: 0.5px; }

  .hero { position: absolute; left: 0; top: 170px; width: 935px; height: 461px; }
  .hero-photo { position: absolute; inset: 0;
    background:
      radial-gradient(ellipse 260px 200px at 720px 90px, rgba(254,194,20,0.55), transparent 70%),
      radial-gradient(ellipse 420px 120px at 470px 360px, rgba(240,170,60,0.55), transparent 70%),
      linear-gradient(180deg, #1b2766 0%, #121735 45%, #2a2318 75%, #6b5a3c 100%); }
  .hero-copy { position: absolute; left: 64px; top: 55px; color: var(--white); }
  .course-title { font-weight: 800; font-size: 33px; line-height: 41px; text-transform: uppercase;
    text-shadow: 0 2px 3px rgba(0,0,0,0.5); }
  .open-class { margin-top: 14px; font-weight: 800; font-size: 24px; text-transform: uppercase; }
  .open-class .label { color: var(--gold); margin-right: 10px; }
  .presenter-intro { margin-top: 18px; font-size: 21px; }
  .presenter-name { margin-top: 6px; font-weight: 800; font-size: 22px; }
  .presenter-name small { font-weight: 400; font-size: 15px; }
  .presenter-role { margin-top: 4px; font-size: 15.5px; line-height: 25px; width: 230px; }

  .venue-photo { position: absolute; left: 656px; top: 452px; width: 238px; height: 238px; border-radius: 50%;
    border: 7px solid var(--gold); background: radial-gradient(circle at 50% 35%, #3e8a4a 0%, #2b6d3a 35%, #1c6fa8 55%, #0d4a86 100%); }

  .info { position: absolute; left: 62px; width: 340px; }
  .info-icon { position: absolute; left: 0; width: 38px; height: 38px; border-radius: 50%; background: var(--ink);
    display: flex; align-items: center; justify-content: center; }
  .info-body { margin-left: 58px; font-size: 16.5px; line-height: 22px; }
  .info-body strong { font-weight: 700; color: var(--ink); }
  .loc { top: 670px; }
  .fee { top: 776px; }
  .fee .amounts { display: inline-block; vertical-align: top; }
  .note { top: 835px; }
  .register { top: 950px; }
  .register .info-body { margin-left: 60px; font-weight: 700; color: var(--ink); line-height: 25px; }
  .register .line { display: flex; align-items: center; gap: 6px; }

  .topics { position: absolute; left: 446px; top: 658px; }
  .topics h2 { font-weight: 800; font-size: 25px; color: var(--gold); text-transform: uppercase; }
  .topic-col { position: absolute; list-style: none; font-size: 16.5px; line-height: 22px; }
  .col-a { left: 446px; top: 698px; width: 225px; }
  .col-b { left: 682px; top: 698px; width: 215px; }
  .topic-col li { position: relative; padding-left: 26px; margin-bottom: 9px; }
  .topic-col li::before { content: ""; position: absolute; left: 0; top: 6px; width: 8px; height: 8px; background: var(--gold); }
  .topic-col li.plain::before { display: none; }

  .footer-bar { position: absolute; left: 0; bottom: 0; width: 935px; height: 46px; background: var(--footer);
    color: var(--white); font-size: 16.5px; display: flex; align-items: center; justify-content: center; }
  .footer-bar b { color: var(--gold); font-weight: 700; }
</style>
</head>
<body>
  <header class="brand-header">
    <span class="brand-mark"></span>
    <span class="brand-name">ROADWISE SAFETY INSTITUTE</span>
  </header>

  <section class="hero">
    <div class="hero-photo" role="img" aria-label="Night highway curving along a hillside with glowing street lamps and light trails"></div>
    <div class="hero-copy">
      <h1 class="course-title">Human Factors in<br>Traffic Crashes, Analysis<br>of Drivers’ Responses –</h1>
      <p class="open-class"><span class="label">Open Class:</span>Manley NSW</p>
      <p class="presenter-intro">Presented by:</p>
      <p class="presenter-name">Grant Pelloway <small>Ph.D.</small></p>
      <p class="presenter-role">World renowned Human Factors expert</p>
    </div>
  </section>
  <div class="venue-photo" role="img" aria-label="Aerial view of a harbour cove with boats, wharf and green headland"></div>

  <div class="info loc">
    <span class="info-icon"><svg width="22" height="22" viewBox="0 0 24 24"><path d="M12 2a7 7 0 0 0-7 7c0 5 7 13 7 13s7-8 7-13a7 7 0 0 0-7-7zm0 9.5A2.5 2.5 0 1 1 12 6.5a2.5 2.5 0 0 1 0 5z" fill="#fec214"/></svg></span>
    <p class="info-body"><strong>Location:</strong><br>Harbourview Lodge – Sydney Harbor National Park, 14 Cliffside Road, Manley NSW</p>
  </div>

  <div class="info fee">
    <span class="info-icon"><svg width="22" height="22" viewBox="0 0 24 24"><rect x="3" y="6" width="18" height="13" rx="2" fill="#fec214"/><rect x="14" y="10" width="7" height="5" fill="#1e1e1e"/></svg></span>
    <p class="info-body"><strong>Course Fee:</strong> <span class="amounts">$1,730 AU<br>$1,200 USD</span></p>
  </div>

  <div class="info note">
    <p class="info-body">It has been 3 years since Dr. Pelloway has come to AU to teach, don’t miss out on this year’s class.</p>
  </div>

  <div class="info register">
    <span class="info-icon"><svg width="22" height="22" viewBox="0 0 24 24"><rect x="3" y="5" width="18" height="12" rx="1" fill="#fec214"/><rect x="1" y="18" width="22" height="2" fill="#fec214"/></svg></span>
    <div class="info-body">
      <p>Register on our website:</p>
      <p class="line"><svg width="16" height="16" viewBox="0 0 24 24"><circle cx="12" cy="12" r="9" fill="none" stroke="#fec214" stroke-width="2.5"/><path d="M3 12h18M12 3c4 4 4 14 0 18M12 3c-4 4-4 14 0 18" fill="none" stroke="#fec214" stroke-width="2"/></svg>www.roadwisesafety.com</p>
      <p>or Contact:</p>
      <p class="line"><svg width="16" height="16" viewBox="0 0 24 24"><rect x="2" y="5" width="20" height="14" fill="#fec214"/><path d="M2 5l10 8 10-8" fill="none" stroke="#fff" stroke-width="2"/></svg>Mara@roadwisesafety.com</p>
      <p class="line"><svg width="16" height="16" viewBox="0 0 24 24"><path d="M6 3l4 4-2 3a12 12 0 0 0 6 6l3-2 4 4-3 3C10 21 3 14 3 6z" fill="#fec214"/></svg>860-555-0142</p>
    </div>
  </div>

  <div class="topics"><h2>Course Topics</h2></div>
  <ul class="topic-col col-a">
    <li>Perception-Response Time</li>
    <li>Response to slow moving or stopped vehicles on multilane high speed roads</li>
    <li>Nighttime recognition</li>
    <li>Headlight mapping demonstration and instruction</li>
    <li>Driver decision making</li>
    <li class="plain">Research in IDRR</li>
    <li>Gap acceptance for left turns, right turns, and through movements for drivers, riders, and pedestrians</li>
  </ul>
  <ul class="topic-col col-b">
    <li>Pedestrian walking speeds</li>
    <li>Acceleration</li>
    <li>Lateral acceleration (swerving) for cars, motorcycles, and commercial vehicles</li>
    <li>Forward and backward acceleration of cars, motorcycles and commercial vehicles</li>
    <li>Drivers’ responses to green and yellow traffic signals, deceleration choice, reaction time and probability of stopping</li>
  </ul>

  <footer class="footer-bar">Visit www.<b>RoadwiseResearch.com</b>/about/to learn more about&nbsp;<b>Dr. Pelloway</b></footer>
</body>
</html>
```